Marke für hochwertige Trauerartikel benötigt Briefpapier
Zielgruppe
Weidkorn ist eine Marke für hochwertige Trauerartikel. Zielgruppe sind Bestattungsunternehmen, die nachhaltig zufriedenen Kunden möchten.
Aufgabenstellung
Wir benötigen Briefpapier: Anschreiben, Rechnngsformular in Farbe und in schwarz weiß. Dazu Visitenkarten und ein gleicherscheinenden E-Mail Absender. Das Design sollte so klar wir möglich sein. Der Druck erfolgt auf recyceltem Papier.

```html
<!DOCTYPE html>
<html lang="de">
<head>
<meta charset="utf-8">
<title>Weidkorn – Visitenkarte</title>
<link href="https://fonts.googleapis.com/css2?family=Montserrat:wght@400;600&display=swap" rel="stylesheet">
<style>
  :root {
    --backdrop: #e4e2de;
    --card-dark: #2b2b2b;
    --card-mid: #3b3b3b;
    --card-back: #232323;
    --gold: #c9a73a;
    --gold-soft: rgba(201, 167, 58, 0.12);
    --pattern-tone: #2d2d2d;
  }
  * { box-sizing: border-box; margin: 0; padding: 0; }
  html, body {
    width: 1200px;
    height: 900px;
    overflow: hidden;
    background: var(--backdrop);
    font-family: "Montserrat", sans-serif;
  }
  .sheet {
    width: 1200px;
    height: 900px;
    display: flex;
    flex-direction: column;
    align-items: center;
    justify-content: center;
    gap: 56px;
  }
  .card {
    position: relative;
    width: 630px;
    height: 360px;
    border-radius: 4px;
    overflow: hidden;
    box-shadow: 0 14px 30px rgba(0, 0, 0, 0.25);
  }
  .card-front {
    background: linear-gradient(160deg, var(--card-mid), var(--card-dark));
  }
  .front-decoration {
    position: absolute;
    top: 0;
    right: 0;
    width: 260px;
    height: 220px;
    background: radial-gradient(circle at 60% 40%, var(--gold-soft), transparent 70%);
  }
  .brand-frame {
    position: absolute;
    left: 48px;
    top: 42px;
    width: 148px;
    height: 118px;
    border: 1.5px solid var(--gold);
    display: flex;
    flex-direction: column;
    align-items: center;
    justify-content: center;
    gap: 12px;
  }
  .brand-square {
    width: 18px;
    height: 18px;
    border: 1.5px solid var(--gold);
  }
  .brand-name {
    color: var(--gold);
    font-weight: 400;
    font-size: 15px;
    letter-spacing: 0.5px;
  }
  .contact {
    position: absolute;
    left: 48px;
    top: 196px;
    color: var(--gold);
  }
  .person-name {
    font-weight: 600;
    font-size: 19px;
    letter-spacing: 1.5px;
    text-transform: uppercase;
  }
  .person-role {
    font-size: 13px;
    margin-top: 3px;
    margin-bottom: 16px;
  }
  .contact-line {
    font-size: 15px;
    line-height: 1.35;
    letter-spacing: 0.3px;
  }
  .card-back {
    background: var(--card-back);
    display: flex;
    align-items: center;
    justify-content: center;
  }
  .back-pattern {
    position: absolute;
    inset: 0;
    background: linear-gradient(150deg, var(--pattern-tone), var(--card-back) 70%);
  }
  .back-brand {
    position: relative;
    display: flex;
    align-items: center;
    gap: 10px;
    color: var(--gold);
    font-size: 20px;
    font-weight: 400;
    letter-spacing: 0.5px;
  }
  .back-brand .brand-square { width: 16px; height: 16px; }
</style>
</head>
<body>
  <main class="sheet">
    <section class="card card-front">
      <div class="front-decoration" role="img" aria-label="Feine goldene Linienornamentik in der oberen rechten Ecke"></div>
      <div class="brand-frame">
        <span class="brand-square"></span>
        <span class="brand-name">Weidkorn</span>
      </div>
      <div class="contact">
        <p class="person-name">Jonas Brenner</p>
        <p class="person-role">Australasian</p>
        <p class="contact-line">254-555-0193</p>
        <p class="contact-line">jbrenner@gestaltwerk-probe.de</p>
        <p class="contact-line">www.gestaltwerk-probe.de</p>
      </div>
    </section>
    <section class="card card-back">
      <div class="back-pattern" role="img" aria-label="Dezentes dunkles Wiederholungsmuster über die gesamte Rückseite"></div>
      <div class="back-brand">
        <span class="brand-square"></span>
        <span>Weidkorn</span>
      </div>
    </section>
  </main>
</body>
</html>
```